New business card design needed for Trucking/Staffing company!

I am looking for a business card design. The business name is Keystone Haul Partners, LLC. This company is a staffing company for commercial drivers/truck drivers. Most of our customers are trucking/supply companies. Our colors are blue/black/white/grey. The info I have on my current business cards is
-Spot for a name
-2 lines for an address
-3 lines for Office, cell, and fax
-email
-website(currently on backside of card with logo but can go anywhere)
Updates

Project Deadline Extended
Reason: Open to more designs

Target Market(s)

Trucking companies, building supply companies

Industry/Entity Type

Business

Contact Information for Business Card

Edgy but professional

Font styles to use
Other font styles liked:
• Open to suggestions

Colors
0555a3
000000
ffffff
9d9d9d

Requirements
Must have
• Must have the logo incorporated

```html
<!DOCTYPE html>
<html lang="en">
<head>
<meta charset="utf-8">
<title>Keystone Haul Partners – Business Card</title>
<link rel="stylesheet" href="https://fonts.googleapis.com/css2?family=Quicksand:wght@500;600;700&display=swap">
<style>
  :root {
    --stage: #2b2b2b;
    --card: #1c1c1d;
    --blue: #0555a3;
    --white: #ffffff;
    --grey: #9d9d9d;
  }
  * { box-sizing: border-box; margin: 0; padding: 0; }
  html, body { width: 1200px; height: 1189px; overflow: hidden; }
  body {
    background: var(--stage);
    font-family: "Quicksand", sans-serif;
    color: var(--white);
    position: relative;
  }
  .card {
    position: absolute;
    left: 250px;
    width: 700px;
    height: 400px;
    background: var(--card);
    border-radius: 26px;
  }
  .card--back { top: 150px; }
  .card--front { top: 640px; }

  .brand {
    display: flex;
    align-items: center;
    gap: 14px;
  }
  .brand__mark {
    width: 22px;
    height: 22px;
    background: var(--blue);
  }
  .brand__name {
    font-weight: 700;
    color: var(--blue);
    letter-spacing: 1px;
    text-transform: uppercase;
  }

  /* back */
  .card--back .brand {
    position: absolute;
    left: 0; right: 0; top: 150px;
    justify-content: center;
  }
  .card--back .brand__name { font-size: 34px; }
  .website {
    position: absolute;
    left: 0; right: 0; top: 250px;
    text-align: center;
    font-size: 22px;
    font-weight: 500;
    letter-spacing: 1px;
  }

  /* front */
  .card--front .brand {
    position: absolute;
    left: 44px; top: 58px;
  }
  .card--front .brand__name { font-size: 30px; }
  .person {
    position: absolute;
    right: 44px; top: 128px;
    text-align: right;
  }
  .person__name {
    font-size: 26px;
    font-weight: 700;
    color: var(--blue);
    text-transform: uppercase;
    letter-spacing: .5px;
  }
  .person__title {
    font-size: 20px;
    font-weight: 500;
    margin-top: -2px;
  }
  .divider {
    position: absolute;
    left: 44px; right: 44px; top: 210px;
    height: 1.5px;
    background: var(--white);
  }
  .contacts {
    position: absolute;
    left: 44px; top: 232px;
    list-style: none;
  }
  .contacts li {
    display: flex;
    align-items: center;
    gap: 12px;
    font-size: 23px;
    font-weight: 500;
    line-height: 34px;
  }
  .icon {
    width: 24px; height: 24px;
    background: var(--blue);
    border-radius: 3px;
    display: flex; align-items: center; justify-content: center;
  }
  .icon svg { width: 16px; height: 16px; }
  .address {
    position: absolute;
    right: 44px; top: 272px;
    text-align: right;
    font-size: 22px;
    font-weight: 500;
    line-height: 32px;
  }
</style>
</head>
<body>
  <section class="card card--back">
    <div class="brand">
      <span class="brand__mark"></span>
      <span class="brand__name">Keystone Haul Partners</span>
    </div>
    <p class="website">www.keystonehaul.com</p>
  </section>

  <section class="card card--front">
    <div class="brand">
      <span class="brand__mark"></span>
      <span class="brand__name">Keystone Haul Partners</span>
    </div>
    <div class="person">
      <p class="person__name">Employee Name</p>
      <p class="person__title">Owner</p>
    </div>
    <div class="divider"></div>
    <ul class="contacts">
      <li><span class="icon"><svg viewBox="0 0 16 16" fill="#fff"><path d="M3 2h3l1 3-2 1a8 8 0 0 0 5 5l1-2 3 1v3c0 1-1 1-1 1A12 12 0 0 1 2 3s0-1 1-1z"/></svg></span>555-201-4400</li>
      <li><span class="icon"><svg viewBox="0 0 16 16" fill="none" stroke="#fff" stroke-width="1.6"><rect x="4.5" y="1.5" width="7" height="13" rx="1"/><line x1="7" y1="12" x2="9" y2="12"/></svg></span>555-201-4401</li>
      <li><span class="icon"><svg viewBox="0 0 16 16" fill="#fff"><rect x="4" y="1" width="8" height="5"/><rect x="1" y="6" width="14" height="6" rx="1"/><rect x="4" y="10" width="8" height="5" stroke="#0555a3" stroke-width="1"/></svg></span>555-201-4402</li>
      <li><span class="icon"><svg viewBox="0 0 16 16" fill="none" stroke="#fff" stroke-width="1.6"><rect x="1.5" y="3.5" width="13" height="9"/><path d="M1.5 3.5l6.5 5 6.5-5"/></svg></span>office@keystonehaul.com</li>
    </ul>
    <p class="address">PO BOX 218<br>linden falls ny 10000</p>
  </section>
</body>
</html>
```